Bramwell Dental personal information forms

We are a Dental Practice that require an update to our information forms, there are 3 versions of it.
I will attach our old ones, we need to keep the same information on there, we just want them to look better and use our current logo and colours.
Our website is www.bramwelldental-example.net
Our facebook is www.facebook.com/bramwelldentalkestonwalk/
..................................................................................................

Target Market(s)

Everyone, easy to read

Industry/Entity Type

Dental Clinic

Colors
0692cd
34a6d7
cee9f5
ffffff
0255a3
3276b5

Requirements
Must have
• Logo
• Our colours
• same information as the uploaded versions
Should not have
• any other colour besides the blues, black and white

```html
<!DOCTYPE html>
<html lang="en">
<head>
<meta charset="utf-8">
<title>Bramwell Dental – Patient Information Form</title>
<link rel="stylesheet" href="https://fonts.googleapis.com/css2?family=Open+Sans:ital,wght@0,400;0,600;0,700;1,400&display=swap">
<style>
  :root{
    --blue:#0692cd;
    --blue-mid:#34a6d7;
    --blue-pale:#cee9f5;
    --blue-deep:#0255a3;
    --blue-steel:#3276b5;
    --paper:#ffffff;
    --ink:#2a2a2a;
    --stage:#2b2b2b;
  }
  *{box-sizing:border-box;margin:0;padding:0}
  html,body{width:1200px;height:900px;overflow:hidden}
  body{background:var(--stage);font-family:"Open Sans",Arial,sans-serif;color:var(--ink)}
  .form-sheet{
    position:absolute;left:290px;top:12px;width:620px;height:876px;
    background:var(--paper);padding:24px 28px 20px;
    display:flex;flex-direction:column;
  }

  /* Header */
  .sheet-header{display:flex;justify-content:space-between;align-items:flex-start}
  .practitioners{margin-top:24px;color:var(--blue-steel);font-size:12px;line-height:1.3}
  .practitioners .role{display:block;text-align:center;font-weight:700;color:var(--blue-deep);font-size:11px;margin-top:2px}
  .brand-name{color:var(--blue);font-weight:600;font-size:30px;letter-spacing:-.5px;line-height:1}
  .header-rule{border-top:2px dotted var(--blue);width:250px;margin:6px 0 0 auto}
  .intro{font-size:7.6px;line-height:1.35;margin-top:4px}
  .intro strong{color:var(--blue-deep)}

  /* Information tables */
  .info-grid{display:flex;justify-content:space-between;margin-top:8px}
  .info-table{border-collapse:collapse;font-size:7.8px;color:var(--blue-deep)}
  .info-table td,.info-table th{border:1px solid var(--blue);height:15px;padding:0 4px;vertical-align:middle}
  .info-table .band{background:var(--blue);color:var(--paper);font-weight:600;font-size:9px;text-align:center;height:16px}
  .info-table .label{width:80px;font-weight:600}
  .info-table .sub{width:28px;font-weight:600}
  .info-table .options{height:17px}
  .option-row{display:flex;justify-content:space-around;font-weight:600}
  .patient-table{width:304px}
  .contact-col{width:248px}
  .contact-col .info-table{width:100%}
  .referred{font-size:8.5px;font-weight:700;color:var(--blue-deep);margin:10px 0 6px}

  /* Questions */
  .question{margin-top:9px}
  .q-line{display:flex;justify-content:space-between;align-items:baseline;font-size:8.8px}
  .yes-no{color:var(--blue-deep);font-weight:700;font-size:8.5px}
  .answer-bar{height:20px;border-radius:10px;background:var(--blue-pale);margin-top:3px;opacity:.75}
  .conditions{display:grid;grid-template-columns:repeat(4,1fr);margin-top:5px;font-size:8.5px}
  .conditions ul{list-style:none}
  .conditions li{display:flex;align-items:center;gap:5px;line-height:1.55}
  .tick-box{width:7px;height:7px;border:1px solid var(--blue-mid);background:var(--blue-pale)}
  strong.em{color:var(--ink)}

  /* Declaration */
  .sheet-rule{border-top:2px dotted var(--blue);width:230px;margin:10px auto 6px}
  .declaration{font-size:7.8px;font-style:italic;line-height:1.45}
  .affirmation{font-size:8.6px;font-weight:700;text-align:center;margin-top:5px;line-height:1.35}
  .sign-row{display:flex;align-items:flex-end;gap:8px;margin-top:auto;color:var(--blue-steel);font-size:10px}
  .sign-line{flex:1;border-bottom:1px solid var(--blue)}
  .date-line{width:110px;border-bottom:1px solid var(--blue)}
</style>
</head>
<body>
<main class="form-sheet">
  <header class="sheet-header">
    <div class="practitioners">Dr. Helen Castellan &amp; Dr. Owen Whitcombe<span class="role">Dental Surgeons</span></div>
    <div class="brand-name">Bramwell Dental</div>
  </header>
  <div class="header-rule"></div>
  <p class="intro"><strong>Welcome back to our practice!</strong><br>
    THIS INFORMATION IS CONFIDENTAL and is necessary to able us to offer you THE BEST POSSIBLE CARE. Because we haven't seen you in some time and because we care about your health status, please take your time and thoroughly complete the following update of your personal and medical information. It is essential that we know about your past and present medical history. Many medical conditions may interfere with dental procedures.</p>

  <section class="info-grid">
    <table class="info-table patient-table">
      <tr><th class="band" colspan="3">Patient Information</th></tr>
      <tr><td class="options" colspan="3"><div class="option-row"><span>Ms</span><span>Mrs</span><span>Miss</span><span>Mr</span><span>Master</span><span>Dr</span><span>Other</span></div></td></tr>
      <tr><td class="label">Surname</td><td colspan="2"></td></tr>
      <tr><td class="label">First Name</td><td colspan="2"></td></tr>
      <tr><td class="label">Preferred</td><td colspan="2"></td></tr>
      <tr><td class="label">Date of Birth</td><td colspan="2"></td></tr>
      <tr><td class="label" rowspan="4">Current<br>Residential<br>Address</td><td colspan="2"></td></tr>
      <tr><td colspan="2"></td></tr>
      <tr><td colspan="2"></td></tr>
      <tr><td class="label" style="width:60px">Postcode</td><td></td></tr>
      <tr><td class="label" rowspan="4">Postal<br>Residential<br>Address<br>(If different)</td><td colspan="2"></td></tr>
      <tr><td colspan="2"></td></tr>
      <tr><td colspan="2"></td></tr>
      <tr><td class="label" style="width:60px">Postcode</td><td></td></tr>
      <tr><td class="label">Occupation</td><td colspan="2"></td></tr>
      <tr><td class="label">Employer</td><td colspan="2"></td></tr>
    </table>

    <div class="contact-col">
      <table class="info-table">
        <tr><th class="band" colspan="5">Patient Information</th></tr>
        <tr><td class="label" rowspan="4">Phone</td><td class="sub">M:</td><td colspan="3"></td></tr>
        <tr><td class="sub">H:</td><td colspan="3"></td></tr>
        <tr><td class="sub">W:</td><td colspan="3"></td></tr>
        <tr><td colspan="4"></td></tr>
        <tr><td class="label">Email</td><td colspan="4"></td></tr>
        <tr><td class="label">Preferred</td><td colspan="4"></td></tr>
        <tr><td class="label" colspan="5">Preferred method of communication</td></tr>
        <tr><td class="options" colspan="5"><div class="option-row"><span>SMS</span><span>Phone</span><span>Email</span><span>Mail</span></div></td></tr>
      </table>
      <p class="referred">Referred by:</p>
      <table class="info-table">
        <tr><th class="band" colspan="2">Emergency Contact</th></tr>
        <tr><td class="label">Name</td><td></td></tr>
        <tr><td class="label">Relationship</td><td></td></tr>
        <tr><td class="label" style="height:22px">Contact<br>Number</td><td></td></tr>
      </table>
    </div>
  </section>

  <section class="question">
    <div class="q-line"><span>Have you taken any prescribed medication or dietary supplements in the last 12 months? If YES, please list bellow.</span><span class="yes-no">YES / NO</span></div>
    <div class="answer-bar"></div>
  </section>
  <section class="question">
    <div class="q-line"><span>Alergies / Reactions? If YES, please list bellow.</span><span class="yes-no">YES / NO</span></div>
    <div class="answer-bar"></div>
  </section>
  <section class="question">
    <div class="q-line"><span>Have you <strong class="em">ever had</strong> or are you <strong class="em">suffering</strong> from any of the following? Please tick any that apply:</span></div>
    <div class="conditions">
      <ul><li><i class="tick-box"></i>Rheumatic fever</li><li><i class="tick-box"></i>Epilepsy</li><li><i class="tick-box"></i>Asthma</li><li><i class="tick-box"></i>Tuberculosis</li><li><i class="tick-box"></i>Radiation Therapy</li><li><i class="tick-box"></i>Dizziness, fainting</li></ul>
      <ul><li><i class="tick-box"></i>Hepatitis A, B or C</li><li><i class="tick-box"></i>Recent eye surgery</li><li><i class="tick-box"></i>Diabetes</li><li><i class="tick-box"></i>Kidney Disease</li><li><i class="tick-box"></i>Heart Attack</li><li><i class="tick-box"></i>High Blood Pressure</li></ul>
      <ul><li><i class="tick-box"></i>Bleeding problems</li><li><i class="tick-box"></i>Artificial joints</li><li><i class="tick-box"></i>Raspiratory problems</li><li><i class="tick-box"></i>HIV Positive</li><li><i class="tick-box"></i>High cholesterol</li><li><i class="tick-box"></i>Cancer</li></ul>
      <ul><li><i class="tick-box"></i>Pace-maker</li><li><i class="tick-box"></i>Osteoporosis</li><li><i class="tick-box"></i>Heart rate problems</li><li><i class="tick-box"></i>Heart murmur</li></ul>
    </div>
  </section>
  <section class="question">
    <div class="q-line"><span>Do you have any disease, condition or problem not listed above?</span><span class="yes-no">YES / NO</span></div>
    <div class="answer-bar"></div>
  </section>
  <section class="question">
    <div class="q-line"><span>Have you had surgery or been to hospital in the last 5 years? If YES, how many months?</span><span class="yes-no">YES / NO</span></div>
    <div class="answer-bar"></div>
  </section>
  <section class="question">
    <div class="q-line"><span>For Women: Are you pregnant? If YES, how many months?</span><span class="yes-no">YES / NO</span></div>
    <div class="answer-bar"></div>
  </section>

  <div class="sheet-rule"></div>
  <p class="declaration">This is to certify that I, the undersigned, consent to the performing of the dental and oral surgery procedures agreed to be necessary or advisable, inluding the use of local anaesthetic as indicated and I will assume responsibility for the fees associated with these procedures. Therefore, I shall pay any legal costs, including solicitor and own costs, tracing costs and any collection commission incurred by Bramwell Dental as a result of my failure to pay any amount due to Bramwell Dental.</p>
  <p class="affirmation">The information that I have provided is to the best of my knowledge true and correct and I understand that is my responsibility<br>to infrom of any changes in my medical status.</p>

  <div class="sign-row">
    <span>Patient/Parent/Person Responsible Signature:</span><span class="sign-line"></span>
    <span>Date:</span><span class="date-line"></span>
  </div>
</main>
</body>
</html>
```